Brightstone Roofing Business Card

This is my current business card. But I’d like to make some changes. Somewhere on the card I’d like to list some of the services we offer. Maybe on the back? But I’d still like to keep the red. White and black modern look.

-residential & commercial roofing
-Roof Repairs & Maintenance
-Storm Damage & Insurance Claims specialist
-Christmas Lights and permanent Christmas lights
Fencing. Windows. Gutters. Siding. Sheetrock, painting.

```html
<!DOCTYPE html>
<html lang="en">
<head>
<meta charset="utf-8">
<title>Brightstone Roofing Business Card</title>
<link rel="stylesheet" href="https://fonts.googleapis.com/css2?family=Exo+2:wght@600;700&family=Lato:wght@400;700&display=swap">
<style>
  :root {
    --page: #ffffff;
    --red: #ad262d;
    --red-dark: #9e2329;
    --red-bright: #e0242c;
    --black: #141414;
    --black-soft: #1f1f1f;
    --white: #ffffff;
    --text-font: "Lato", Arial, sans-serif;
    --display-font: "Exo 2", Arial, sans-serif;
  }
  * { margin: 0; padding: 0; box-sizing: border-box; }
  html, body { width: 1200px; height: 1000px; overflow: hidden; background: var(--page); }
  .canvas { position: relative; width: 1200px; height: 1000px; }

  .card { position: absolute; left: 196px; width: 808px; height: 462px; border-radius: 22px; overflow: hidden; }
  .card-front { top: 30px; background: linear-gradient(160deg, var(--red-dark) 0%, var(--red) 55%, #b2242b 100%); }
  .card-back { top: 508px; background: radial-gradient(ellipse at 40% 40%, var(--black-soft) 0%, var(--black) 75%); }

  .brand-mark { position: absolute; border-radius: 50%; }
  .card-front .brand-mark { left: 264px; top: 48px; width: 280px; height: 280px; background: var(--red-bright); border: 6px solid var(--white); }
  .brand-name { position: absolute; font-family: var(--text-font); font-weight: 700; color: var(--white); text-align: center; text-transform: uppercase; letter-spacing: 1px; }
  .card-front .brand-name { left: 0; right: 0; top: 352px; font-size: 30px; line-height: 38px; }

  .holder { position: absolute; left: 33px; top: 38px; }
  .holder-name { font-family: var(--display-font); font-weight: 700; font-size: 30px; letter-spacing: 1.5px; color: var(--white); text-transform: uppercase; line-height: 34px; }
  .holder-name .first { color: var(--red-bright); }
  .holder-role { font-family: var(--text-font); font-size: 20px; color: var(--white); margin-top: 2px; }
  .holder-role .region { color: var(--red-bright); }

  .contacts { position: absolute; left: 484px; top: 35px; list-style: none; }
  .contacts li { display: flex; align-items: center; height: 29px; font-family: var(--text-font); font-size: 21px; letter-spacing: 0.8px; color: var(--white); }
  .contacts svg { width: 15px; height: 15px; margin-right: 9px; fill: var(--red-bright); }

  .card-back .brand-mark { left: 536px; top: 162px; width: 190px; height: 190px; background: var(--red-bright); border: 6px solid var(--white); }
  .card-back .brand-name { left: 480px; width: 302px; top: 370px; font-size: 22px; line-height: 28px; }

  .services { position: absolute; left: 28px; top: 298px; list-style: none; }
  .services li { display: flex; align-items: center; height: 25.5px; font-family: var(--text-font); font-weight: 700; font-size: 18px; color: var(--white); }
  .services .bullet { width: 10px; height: 10px; margin-right: 9px; display: grid; grid-template-columns: 4px 4px; gap: 2px; }
  .services .bullet i { background: var(--red-bright); }
</style>
</head>
<body>
<main class="canvas">
  <section class="card card-front" aria-label="Card front">
    <div class="brand-mark"></div>
    <p class="brand-name">Brightstone<br>Roofing Co.</p>
  </section>

  <section class="card card-back" aria-label="Card back">
    <div class="holder">
      <h1 class="holder-name"><span class="first">Dean</span> Carver</h1>
      <p class="holder-role">Roofing contractor in <span class="region">Texas</span></p>
    </div>

    <ul class="contacts">
      <li><svg viewBox="0 0 16 16"><path d="M3.5 1l2.5 3-1.5 2c1 2 3 4 5 5l2-1.5 3 2.5-1.5 2.5C7 15 1 9 1 2.5z"/></svg>682 - 555 - 0148</li>
      <li><svg viewBox="0 0 16 16"><path d="M15 1L1 7l5 2 1 5 2.5-3.5L13 13z"/></svg>Dean@brightstoneroofing.co</li>
      <li><svg viewBox="0 0 16 16"><circle cx="8" cy="8" r="6.5" fill="none" stroke="#e0242c" stroke-width="1.6"/><path d="M1.5 8h13M8 1.5c-3 3.5-3 9.5 0 13M8 1.5c3 3.5 3 9.5 0 13" fill="none" stroke="#e0242c" stroke-width="1.3"/></svg>www.brightstoneroofing.co</li>
    </ul>

    <div class="brand-mark"></div>
    <p class="brand-name">Brightstone Roofing Co.</p>

    <ul class="services">
      <li><span class="bullet"><i></i><i></i><i></i><i></i></span>Residential &amp; commercial roofing</li>
      <li><span class="bullet"><i></i><i></i><i></i><i></i></span>Roof Repairs &amp; Maintenance</li>
      <li><span class="bullet"><i></i><i></i><i></i><i></i></span>Storm Damage &amp; Insurance Claims specialist</li>
      <li><span class="bullet"><i></i><i></i><i></i><i></i></span>Christmas Lights &amp; permanent Christmas lights</li>
      <li><span class="bullet"><i></i><i></i><i></i><i></i></span>Fencing. Windows. Gutters. Siding. Sheetrock, painting</li>
    </ul>
  </section>
</main>
</body>
</html>
```